I need a feather flag designed for my business which states " HELICOPTER RIDES" and possibly adding my logo to them. This will be used for my helicopter ride business and we can put these up to show people where the rides will be .

Industry/Entity Type

aviation

Colors
00AB8E
00BBA5
67D7C9
C6EFE9
E9F9F6
EB3D1F
EC4F4E
F09395
F8D3D4
FCEDEE

Requirements
Must have
• logo

```html
<!DOCTYPE html>
<html lang="en">
<head>
<meta charset="UTF-8">
<title>Helicopter Rides Feather Flag</title>
<link rel="stylesheet" href="https://fonts.googleapis.com/css2?family=Oswald:wght@500&display=swap">
<style>
  :root {
    --backdrop: #b3b3b3;
    --flag-white: #ededed;
    --ink-navy: #141723;
    --accent-red: #d9140f;
    --base-black: #080808;
    --photo-dark: #2f3238;
    --photo-mid: #56606a;
    --photo-sky: #8fa4b3;
  }
  html, body {
    margin: 0;
    padding: 0;
    width: 1200px;
    height: 1001px;
    overflow: hidden;
    background: var(--backdrop);
  }
  .stage {
    width: 1200px;
    height: 1001px;
    display: flex;
    align-items: center;
    justify-content: center;
  }
  .feather-flag {
    height: 880px;
    width: auto;
    display: block;
  }
  .flag-body { fill: var(--flag-white); }
  .flag-headline {
    font-family: 'Oswald', sans-serif;
    font-weight: 500;
    font-size: 100px;
    letter-spacing: 0;
  }
  .headline-main { fill: var(--ink-navy); }
  .headline-accent { fill: var(--accent-red); }
  .flag-base-band { fill: var(--base-black); }
</style>
</head>
<body>
  <main class="stage">
    <svg class="feather-flag" viewBox="0 0 218 782" xmlns="http://www.w3.org/2000/svg">
      <defs>
        <linearGradient id="cockpitTones" x1="0" y1="0" x2="1" y2="1">
          <stop offset="0" stop-color="var(--photo-dark)"/>
          <stop offset="0.55" stop-color="var(--photo-mid)"/>
          <stop offset="0.8" stop-color="var(--photo-sky)"/>
          <stop offset="1" stop-color="var(--photo-dark)"/>
        </linearGradient>
        <clipPath id="flagShape">
          <path d="M0,782 L0,220 C0,90 100,0 218,0 L218,782 Z"/>
        </clipPath>
      </defs>

      <g clip-path="url(#flagShape)">
        <path class="flag-body" d="M0,782 L0,220 C0,90 100,0 218,0 L218,782 Z"/>

        <g class="flag-photo" role="img" aria-label="Photo from inside a helicopter cockpit: instrument panel, pilot's legs and a mountain valley through the windscreen">
          <polygon points="0,492 218,545 218,752 0,695" fill="url(#cockpitTones)"/>
        </g>

        <polygon class="flag-base-band" points="0,702 218,778 218,782 0,782"/>
      </g>

      <text class="flag-headline" transform="translate(150,507) rotate(-90)" textLength="395" lengthAdjust="spacingAndGlyphs"><tspan class="headline-main">HELICOPTER </tspan><tspan class="headline-accent">RIDES</tspan></text>
    </svg>
  </main>
</body>
</html>
```